Business cards

I would like a black background with the design I previously chose. I need 2 sets of cards. Mine will have Marisol Brandt, Broker/Owner, 307-555-0148 and marisol.harborpeak@mailvista.com
The second set will read, Dana Rutledge, Realtor 307-555-0172, dana.harborpeak@mailvista.com

Industry/Entity Type

Business

```html
<!DOCTYPE html>
<html lang="en">
<head>
<meta charset="utf-8">
<title>Business Cards – Marisol Brandt &amp; Dana Rutledge</title>
<link rel="stylesheet" href="https://fonts.googleapis.com/css2?family=Archivo:wght@400;700&display=swap">
<style>
  :root {
    --backdrop: #a0a1a4;
    --card: #000000;
    --text: #ffffff;
    --gold: #e0a814;
    --green: #6e8c43;
  }
  * { box-sizing: border-box; margin: 0; padding: 0; }
  html, body {
    width: 1200px;
    height: 930px;
    overflow: hidden;
    background: var(--backdrop);
    font-family: "Archivo", Arial, sans-serif;
  }
  .sheet { position: relative; width: 1200px; height: 930px; }
  .card {
    position: absolute;
    left: 353px;
    width: 494px;
    height: 304px;
    background: var(--card);
    color: var(--text);
  }
  .card--broker { top: 130px; --accent: var(--gold); }
  .card--realtor { top: 495px; --accent: var(--green); }

  .card__identity {
    position: absolute;
    right: 40px;
    top: 95px;
    text-align: right;
  }
  .card__name {
    font-weight: 700;
    font-size: 19.5px;
    line-height: 22px;
    color: var(--accent);
  }
  .card__role {
    font-weight: 400;
    font-size: 14px;
    line-height: 18px;
    margin-top: 1px;
  }
  .card__band {
    position: absolute;
    left: 0;
    top: 142px;
    width: 100%;
    height: 22px;
    background: var(--accent);
  }
  .card__contacts {
    position: absolute;
    right: 40px;
    top: 177px;
    list-style: none;
  }
  .contact {
    display: flex;
    align-items: center;
    justify-content: flex-end;
    height: 24px;
    margin-bottom: 3px;
    font-size: 13.5px;
    font-weight: 400;
  }
  .contact__icon {
    width: 24px;
    height: 24px;
    margin-left: 12px;
    flex: none;
  }
</style>
</head>
<body>
<main class="sheet">

  <section class="card card--broker">
    <div class="card__identity">
      <p class="card__name">Marisol Brandt</p>
      <p class="card__role">Broker/Owner</p>
    </div>
    <div class="card__band"></div>
    <ul class="card__contacts">
      <li class="contact">
        <span class="contact__text">307-555-0148</span>
        <svg class="contact__icon" viewBox="0 0 24 24" aria-hidden="true">
          <rect x="0.5" y="0.5" width="23" height="23" fill="none" stroke="var(--gold)"/>
          <rect x="2.5" y="2.5" width="19" height="19" fill="var(--gold)"/>
          <path d="M7.6 5.8l2 2.2-1.1 1.6c.8 1.9 2.2 3.4 4 4.3l1.6-1.1 2.3 2-1.3 2c-4.6-.2-8.9-4.4-9.3-9.1z" fill="#fff"/>
        </svg>
      </li>
      <li class="contact">
        <span class="contact__text">marisol.harborpeak@mailvista.com</span>
        <svg class="contact__icon" viewBox="0 0 24 24" aria-hidden="true">
          <rect x="0.5" y="0.5" width="23" height="23" fill="none" stroke="var(--gold)"/>
          <rect x="2.5" y="2.5" width="19" height="19" fill="var(--gold)"/>
          <rect x="5.5" y="7.5" width="13" height="9" fill="#fff"/>
          <path d="M5.5 7.5l6.5 5 6.5-5M5.5 16.5l4.8-4.2M18.5 16.5l-4.8-4.2" fill="none" stroke="var(--gold)" stroke-width="0.8"/>
        </svg>
      </li>
    </ul>
  </section>

  <section class="card card--realtor">
    <div class="card__identity">
      <p class="card__name">Dana Rutledge</p>
      <p class="card__role">Realtor</p>
    </div>
    <div class="card__band"></div>
    <ul class="card__contacts">
      <li class="contact">
        <span class="contact__text">307-555-0172</span>
        <svg class="contact__icon" viewBox="0 0 24 24" aria-hidden="true">
          <rect x="0.5" y="0.5" width="23" height="23" fill="none" stroke="var(--green)"/>
          <rect x="2.5" y="2.5" width="19" height="19" fill="var(--green)"/>
          <path d="M7.6 5.8l2 2.2-1.1 1.6c.8 1.9 2.2 3.4 4 4.3l1.6-1.1 2.3 2-1.3 2c-4.6-.2-8.9-4.4-9.3-9.1z" fill="#fff"/>
        </svg>
      </li>
      <li class="contact">
        <span class="contact__text">dana.harborpeak@mailvista.com</span>
        <svg class="contact__icon" viewBox="0 0 24 24" aria-hidden="true">
          <rect x="0.5" y="0.5" width="23" height="23" fill="none" stroke="var(--green)"/>
          <rect x="2.5" y="2.5" width="19" height="19" fill="var(--green)"/>
          <rect x="5.5" y="7.5" width="13" height="9" fill="#fff"/>
          <path d="M5.5 7.5l6.5 5 6.5-5M5.5 16.5l4.8-4.2M18.5 16.5l-4.8-4.2" fill="none" stroke="var(--green)" stroke-width="0.8"/>
        </svg>
      </li>
    </ul>
  </section>

</main>
</body>
</html>
```